Everyone did such an amazing job on the website design. Thank you very much. I'm sorry we couldn't pick all of them. Thank you again for your hard work.
Designers, thank you for all of your hard work! These designs are incredible. We are evaluating each draft and trying to provide each of you very thorough feedback. Because there are now multiple versions of your designs, we are only keeping the ones we like the best and eliminating the others. Please review page 3 on the mockup. We will need this page designed because it will be standard for all of our product pages.
torvanel- we like the simplistic feel of your design. We also love how you have made the slideshow feature the main focal point of the site. However, can you replace the picture of the girl with the picture of the Harbor Lens product that was included within the mockup? We need to see how the product will look on the site. We feel like the two sections, Business Intelligence and Welcome get lost because it is in the area of the product feature. That area needs to reworked so the reader will look at the product feature but also go to those sections. Can you make the font color brighter on the tabs? Also, please use the logo with the black background. Thank you for your design!
kpo7data-We really like your draft #7. We like that you have featured and highlighted the social media icons, the contact us, and the news information and that they do not take away from the rest of the site. What we would change is the texture within the background of the site. There are a lot of competing textures and while we like them, there are too many. Also, can you make the business intelligence section stand out a little more?
merudo-we like both your drafts 2 & 3. If we could find a way to combine them, then it would be great! We like the simple feel of draft 3 but draft 2 has a lot of features we like.
Draft 2:
-Prefer this slideshow layout over draft 3
-Like the use of a telephone rather than using the phrase "call us"
-Like the social media icons placement better in draft 2 because they are more prominent and do not get lost on the site
-Like the small section that says "Welcome to m7v solutions". It is very brief but tells the audience who we are.
-Like that the news is featured. This section is too large though.
-Love the "Our services" section with the graphics and small summary of each. However, we only offer two products under Market Research, which is Competitor Research and Industry Research. Therefore, we should only have two options: Option 1-Just list "Market Research" or Option 2: just list "Competitor Research" and "Industry Research". We cannot have all three at the same time.
-Remove the smarter research box
-We only have pages: Business Intelligence, About Us,Buzz, Blog, Client Login, and Support. Please remove all the additional tabs.
-Like that the join our mailing list is featured but should be smaller. While it is important, it is not a significant feature of the site.
-Needs to include company address.
Draft 3:
-Like that you incorporated our logo in the news section
-Like the simple look and feel of this one
-Like that support and client login is in a separate location and easier to find.
merudo-I'm going to have to eliminate draft #1 because there is too much content. We want the readers' eyes to really focus on the featured product. We found this draft to offer too many options and that the reader may get lost on where to go.
frovak1973- I like your draft #4. A couple of changes though:
-Please switch out the logo with the company one rather than using the blog logo.
-Please replace the background color to the phone number with one of the colors from the logo.
-Can you do something more creative with the news section?
-The social media icons get lost and don't seem to be very important. Can you feature them a little more?
-There needs to be a section with a join our mailing list
brightwaves-I like how draft #8 incorporates the colors from the logo. I think it ties the logo in with the website. I would like to see the social media icons stand out more. Also, I would like to make the phone number stand out because we do not have a "contact" us page. Also, can I see the website reversed with a black background rather than a white? Thank you!
Designers, the mockup of the website is a document to give you an idea of how we are anticipating the site to be setup in regards to amount of pages, etc. We do not need all the pages to be created. The document is just for your reference. Thanks!
Thank you for all your hard work and efforts!
Thank you for your design!
1. black: Linear gradient from (C=0, M=0, Y=0, K=30)to (C=0, M=0, Y=0, K=80)
2. gray: (C=0, M=0, Y=0, K=70)
3. red: (C=0, M=100, Y=100, K=70)
4. purple: (C=47, M=83, Y=33, K=1)
5. blue: (C=40, M=0, Y=0, K=70)
6. dark green: (C=100, M=0, Y=100, K=0)
6. light green: (C=30, M=0, Y=88, K=0)
fonts =
1. MicrogammaDEEMedExt
2. MyriadPro

```html
<!DOCTYPE html>
<html lang="en">
<head>
<meta charset="utf-8">
<title>m7v solutions – Market Insight for Growing Teams</title>
<link rel="stylesheet" href="https://fonts.googleapis.com/css2?family=Bebas+Neue&family=PT+Sans:wght@400;700&display=swap">
<style>
:root{
  --ink:#0b0b0b;
  --box:#161616;
  --grey:#8a8a8a;
  --grey-light:#bdbdbd;
  --white:#f2f2f2;
  --red:#e0262a;
  --green:#9ccb3b;
  --blue:#5cb4dc;
  --ui:"PT Sans", Arial, sans-serif;
  --display:"Bebas Neue", Impact, sans-serif;
}
*{box-sizing:border-box;margin:0;padding:0}
html,body{width:1200px;height:876px;overflow:hidden;background:var(--ink)}
body{font-family:var(--ui);color:var(--grey-light);position:relative}
a{text-decoration:none}

.site-header{position:absolute;left:0;top:0;width:1200px;height:98px;
  background:linear-gradient(#2a2a2a,#151515)}
.brand-name{position:absolute;left:130px;top:22px;font-size:38px;font-weight:700;color:var(--white);line-height:1}
.brand-tagline{position:absolute;left:131px;top:66px;font-size:14px;color:var(--grey-light);font-weight:700}

.utility-tabs{position:absolute;left:870px;top:0;display:flex;gap:6px}
.utility-tabs a{display:block;background:#050505;color:var(--white);font-size:14px;
  padding:6px 18px;border-radius:0 0 4px 4px}
.phone{position:absolute;left:884px;top:48px;display:flex;align-items:center;gap:10px;
  font-size:25px;color:var(--white)}

.main-nav{position:absolute;left:0;top:98px;width:1200px;height:36px;
  background:linear-gradient(#333,#1d1d1d);border-top:1px solid #444;border-bottom:1px solid #000}
.main-nav ul{list-style:none;position:absolute;left:130px;top:9px;display:flex;gap:30px}
.main-nav a{color:var(--white);font-weight:700;font-size:15px;letter-spacing:.3px}
.search{position:absolute;left:880px;top:6px;width:190px;height:24px;background:#111;
  border:1px solid #444;border-radius:3px;font-size:12px;color:var(--grey);padding:4px 8px}
.search svg{position:absolute;right:6px;top:5px}

.slideshow{position:absolute;left:0;top:134px;width:1200px;height:402px;
  background:radial-gradient(ellipse at 60% 40%,#1d1d1d,#050505 75%)}
.slide-visual{position:absolute;left:125px;top:28px;width:335px;height:305px;
  background:linear-gradient(135deg,#f4f4f4 0%,#dcdcdc 55%,#9a9a9a 100%);
  border:6px solid #2b2b2b;border-radius:4px;box-shadow:0 14px 30px rgba(0,0,0,.7)}
.slide-headline{position:absolute;left:508px;top:84px;font-family:var(--display);font-weight:400;
  font-size:58px;line-height:58px;color:#9b9b9b;letter-spacing:1px}
.slide-headline .accent{color:var(--red);display:block;margin-top:8px}
.read-more{position:absolute;left:775px;top:305px;width:95px;height:26px;border-radius:13px;
  background:#1f1f1f;border:1px solid #3a3a3a;color:var(--white);font-size:12px;
  display:flex;align-items:center;justify-content:center;gap:10px}
.slide-dots{position:absolute;left:1006px;top:372px;display:flex;gap:10px}
.slide-dots span{width:7px;height:7px;border-radius:50%;background:#777}
.slide-dots span.active{background:var(--green)}

.blog-tab{position:absolute;z-index:5;left:0;top:472px;width:34px;height:84px;background:var(--green);
  border-radius:0 4px 4px 0;display:flex;align-items:center;justify-content:center}
.blog-tab span{transform:rotate(-90deg);font-weight:700;font-size:16px;color:#1b2a05;letter-spacing:1px}

.intro{position:absolute;left:0;top:536px;width:1200px;height:154px;background:var(--ink)}
.welcome{position:absolute;left:130px;top:26px;width:400px}
.welcome h2{font-weight:400;font-size:25px;color:var(--green);margin-bottom:10px}
.welcome p{font-size:14px;line-height:17px;color:var(--grey-light)}
.welcome strong{color:var(--blue)}
.service{position:absolute;top:26px}
.service h3{font-weight:400;font-size:25px;color:var(--white);margin-bottom:10px}
.service .thumb{position:absolute;top:44px;left:0;width:44px;height:64px;border-radius:4px}
.service p{margin-left:54px;font-size:11px;line-height:13px;color:var(--grey)}
.service p em{font-style:normal;color:var(--white);display:block;margin-top:2px}
.service.competitor{left:568px;width:210px}
.service.industry{left:830px;width:240px}
.thumb.chess{background:linear-gradient(#e8e8e8,#6f6f6f)}
.thumb.factory{background:linear-gradient(#d9d9d9,#7a7a7a)}

.info-band{position:absolute;left:0;top:690px;width:1200px;height:152px;
  background:linear-gradient(#2d2d2d,#1e1e1e);border-top:1px solid #444}
.info-col{position:absolute;top:12px}
.info-col h4{font-size:15px;color:var(--white);font-weight:700;margin-bottom:14px}
.info-box{background:var(--box);border:1px solid #0a0a0a;border-radius:3px;padding:10px 14px;
  height:84px;font-size:13px;line-height:16px;color:var(--grey-light)}
.info-box b{color:var(--white);display:block;font-size:14px;margin-bottom:2px}
.news{left:130px;width:296px}
.contact{left:445px;width:306px}
.follow{left:770px;width:300px}
.social{display:flex;gap:16px;margin:22px 0 0 14px}
.social span{width:34px;height:34px;border-radius:5px}
.social .fb{background:#3b5a98}
.social .tw{background:#2aa9e0}
.social .li{background:#1c7ab5}
.social .gp{background:#c8412f}
.social .rss{background:#7bb43b;border-radius:50%}

.site-footer{position:absolute;left:0;top:842px;width:1200px;height:34px;background:#050505;
  font-size:12px;color:var(--grey-light);display:flex;align-items:center}
.site-footer nav{position:absolute;left:130px;display:flex;gap:10px}
.site-footer .sep{color:#555}
.site-footer .contact-line{position:absolute;right:130px}
</style>
</head>
<body>

<header class="site-header">
  <div class="brand-name">m7v solutions</div>
  <div class="brand-tagline">Market Insight for Growing Teams</div>
  <nav class="utility-tabs"><a href="#">Support</a><a href="#">Client Login</a></nav>
  <div class="phone">
    <svg width="22" height="22" viewBox="0 0 24 24"><path fill="#9ccb3b" d="M6.6 10.8a15 15 0 0 0 6.6 6.6l2.2-2.2a1 1 0 0 1 1-.25 11.4 11.4 0 0 0 3.6.57 1 1 0 0 1 1 1V20a1 1 0 0 1-1 1A17 17 0 0 1 3 4a1 1 0 0 1 1-1h3.5a1 1 0 0 1 1 1c0 1.25.2 2.45.57 3.57a1 1 0 0 1-.25 1z"/></svg>
    <span>555-210-4477</span>
  </div>
</header>

<nav class="main-nav">
  <ul>
    <li><a href="#">BUSINESS INTELLIGENCE</a></li>
    <li><a href="#">ABOUT US</a></li>
    <li><a href="#">BUZZ</a></li>
    <li><a href="#">BLOG</a></li>
  </ul>
  <div class="search">Enter Search Here...
    <svg width="12" height="12" viewBox="0 0 12 12"><circle cx="5" cy="5" r="3.6" fill="none" stroke="#aaa" stroke-width="1.5"/><path d="M7.6 7.6 11 11" stroke="#aaa" stroke-width="1.6"/></svg>
  </div>
</nav>

<section class="slideshow">
  <div class="slide-visual" role="img" aria-label="Product screenshot of the Competitive Intelligence web page shown in a browser window"></div>
  <h1 class="slide-headline">DO YOU KNOW WHAT YOUR<br>COMPETITORS ARE DOING?<span class="accent">WE DO.</span></h1>
  <div class="read-more">READ MORE
    <svg width="6" height="8" viewBox="0 0 6 8"><path d="M0 0 6 4 0 8z" fill="#fff"/></svg>
  </div>
  <div class="slide-dots"><span class="active"></span><span></span><span></span></div>
</section>

<a class="blog-tab" href="#"><span>BLOG</span></a>

<section class="intro">
  <div class="welcome">
    <h2>Welcome to m7v solutions</h2>
    <p>We're an integrated market research and agency. We are results-driven. All our marketing campaigns are focused on delivering results that will build your business &amp; we won't settle for anything less. We provide all our clients <strong>I want smarter research.</strong></p>
  </div>
  <div class="service competitor">
    <h3>Competitor Intel</h3>
    <div class="thumb chess" role="img" aria-label="Chess piece illustration"></div>
    <p>In condimentum facilisis porta. Sed nec diam eu diam mattis viverra. Nulla magna diam porttitor.<em>Read More...</em></p>
  </div>
  <div class="service industry">
    <h3>Industry Intel</h3>
    <div class="thumb factory" role="img" aria-label="Factory building illustration"></div>
    <p>In condimentum facilisis porta. Sed nec diam eu diam mattis viverra. Nulla magna diam porttitor.<em>Read More...</em></p>
  </div>
</section>

<section class="info-band">
  <div class="info-col news">
    <h4>m7v News</h4>
    <div class="info-box"><b>June 21, 2012</b>m7v solutions attends Data Summit Conference in Tampa, FL</div>
  </div>
  <div class="info-col contact">
    <h4>Contact Us</h4>
    <div class="info-box">m7v solutions<br>4410 Alder Bend Rd<br>Tampa, FL 33600</div>
  </div>
  <div class="info-col follow">
    <h4>Follow Us</h4>
    <div class="social" aria-label="Social media links">
      <span class="fb"></span><span class="tw"></span><span class="li"></span><span class="gp"></span><span class="rss"></span>
    </div>
  </div>
</section>

<footer class="site-footer">
  <nav>
    <span>Market Research</span><span class="sep">|</span>
    <span>Design Services</span><span class="sep">|</span>
    <span>About Us</span><span class="sep">|</span>
    <span>Support</span><span class="sep">|</span>
    <span>Client Login</span><span class="sep">|</span>
    <span>Buzz</span>
  </nav>
  <div class="contact-line">Email: info@m7vintel.com &nbsp;|&nbsp; 555-210-4477</div>
</footer>

</body>
</html>
```